Executive Presence Book Cover for Larkmoor Coaching

I am looking for 10 book covers that are unified and work very well together. they have to be simple with an international feel.I will be using the colors of the rainbows for the color of the books and all I am looking for is a creative way to write the title of the book on the cover. The ten titles are as follows: Transparency, Humility, Poise ,Charisma ,Relationships, Results, Clarity, Being Present, Grooming and Appearance,Acumen

Target Market(s)

business executives

Font styles to use
Other font styles liked:
• use any font you think would work

Colors

Designer to choose colors to be used in the design.

Requirements
Must have
• simple, easy to read, looking for the word to be the focus/focal point of the cover. we will be putting information on the back cover of our company etc.
• only the words of the title nothing else. The size of the book is 9“ x 7“. The only thing on the outside of the book is the title, no author nothing else. We will be putting information on the back cover of the book in very simple font.
Nice to have
• i would like each title of the 10 book covers to be clean, consistent and elegant and corporate. as long as it is not too "SILLY" i would like the titles to speak of their purpose. for instance,
• charisma could have a letter that look elegant
• being present could have some bold letters.
Should not have
• alot of drawings or pictures
• they can't be jovial, light or humorous treatments.

```html
<!DOCTYPE html>
<html lang="en">
<head>
<meta charset="utf-8">
<title>Humility — Larkmoor Coaching Book Cover</title>
<link rel="stylesheet" href="https://fonts.googleapis.com/css2?family=Kaushan+Script&display=swap">
<style>
  :root {
    --page-bg: #1f1f1f;
    --sky-top: #08495a;
    --sky-mid: #0b6679;
    --sky-low: #1487a6;
    --sky-glow: #3aa8d2;
    --sky-haze: #4f8ea6;
    --title-ink: #ffffff;
    --title-shadow: rgba(0, 20, 28, 0.75);
  }
  html, body {
    margin: 0;
    padding: 0;
    width: 1145px;
    height: 1200px;
    overflow: hidden;
    background: var(--page-bg);
  }
  .book-cover {
    position: absolute;
    left: 130px;
    top: 30px;
    width: 886px;
    height: 1140px;
    overflow: hidden;
  }
  .cover-sky {
    position: absolute;
    inset: 0;
    background:
      radial-gradient(ellipse 55% 35% at 28% 92%, var(--sky-glow) 0%, rgba(58,168,210,0) 100%),
      radial-gradient(ellipse 60% 30% at 85% 95%, var(--sky-haze) 0%, rgba(79,142,166,0) 100%),
      linear-gradient(180deg, var(--sky-top) 0%, var(--sky-mid) 35%, var(--sky-mid) 55%, var(--sky-low) 85%, var(--sky-haze) 100%);
  }
  .cover-title {
    position: absolute;
    left: 0;
    right: 0;
    top: 120px;
    margin: 0;
    text-align: center;
    font-family: "Kaushan Script", cursive;
    font-weight: 400;
    font-size: 196px;
    line-height: 1;
    color: var(--title-ink);
    transform: rotate(-4deg);
    text-shadow: 3px 4px 0 var(--title-shadow), 0 0 14px rgba(255,255,255,0.25);
    letter-spacing: -2px;
  }
</style>
</head>
<body>
  <main class="book-cover">
    <div class="cover-sky" role="img" aria-label="Teal starry nebula sky texture filling the cover"></div>
    <h1 class="cover-title">Humility</h1>
  </main>
</body>
</html>
```